Facebook Cover & Profile Branding for OlvendrA Technologies

We need a modern, premium Facebook cover image for our company Olvendra Technologies GmbH. The design should be clean, professional, and aligned with our corporate colors (neon green and deep blue) as well as our logo. It should clearly represent us as a technology and IT consulting company with a strong focus on software testing and quality assurance.

Since Olvendra Technologies is also active in the U.S. market, the design may include global or U.S.-related elements (e.g., subtle references to international presence, tech innovation with a global reach).

Requirements:

Integration of the Olvendra logo and brand colors

Modern, premium look with a tech-driven feel

Clear, simple layout that looks good on desktop and mobile

Optional: subtle U.S./international references to highlight our global presence

Goal:
A professional, eye-catching Facebook cover image that strengthens our brand identity and reflects our international expansion into the U.S. market.

Target Market(s)

Medium to large enterprises in the technology, finance, and energy sectors - Companies looking for premium IT consulting, software testing, and quality assurance services - Decision makers and executives (CIOs, CTOs, IT managers) in Europe and the United States - A global audience that values innovation, professionalism, and trust

Industry/Entity Type

Information Technology & Consulting Software Testing & Quality Assurance Technology / Professional Services Global IT Consulting with U.S. Market Presence

Requirements
Must have
• Integration of the Olvendra Technologies logo and brand colors (Neon Green & Deep Blue) Modern, premium design with a strong tech-oriented look and feel Clean and professional layout, optimized for both desktop and mobile display Clear visibility of the brand identity (technology, IT consulting, software testing, quality assurance) Subtle reference to U.S. presence / global expansion (to highlight activity in both Germany and the U.S.) Balanced use of colors and space for a high-end, corporate appearance
Nice to have
• Subtle animations or motion effects (e.g., light gradients, moving lines, glowing accents) Dark/Light version option for different moods or seasonal campaigns Integration of social media icons (LinkedIn, Instagram, Facebook) in a clean, minimal way Tech-inspired background elements (digital patterns, abstract shapes, network grids) Space for an optional tagline or slogan (e.g., “Innovation. Quality. Global Impact.”) Adaptability for other platforms (so the design style can be reused for LinkedIn or Twitter headers)
Should not have
• Cluttered or overloaded layouts that reduce clarity Low-quality stock photos or generic imagery that doesn’t fit a premium brand Use of colors outside the Olvendra brand identity (Neon Green & Deep Blue) Outdated design styles (e.g., heavy gradients, 3D effects, drop shadows) Complex text blocks that make the design look busy Elements that distract from the logo and core brand message Pop-art or playful styles that don’t match the premium, professional tech look

```html
<!DOCTYPE html>
<html lang="en">
<head>
<meta charset="utf-8">
<title>Olvendra Technologies GmbH — Facebook Cover</title>
<link rel="stylesheet" href="https://fonts.googleapis.com/css2?family=Montserrat:wght@500;800&family=Roboto:wght@400&display=swap">
<style>
  :root {
    --page-bg: #ececec;
    --cover-black: #060607;
    --green-tint: #0d2a17;
    --teal-tint: #0a2228;
    --neon-green: #3cf23a;
    --aqua: #10d3c4;
    --deep-blue: #1f6fe0;
    --white: #ffffff;
    --contact-blue: #2b7cc0;
    --profile-grey-a: #c4c3c7;
    --profile-grey-b: #bdbcc1;
    --ink-dark: #111214;
  }
  * { box-sizing: border-box; margin: 0; padding: 0; }
  html, body {
    width: 1200px; height: 800px; overflow: hidden;
    background: var(--page-bg);
  }
  .cover {
    position: absolute; left: 86px; top: 146px;
    width: 1033px; height: 473px;
    background: var(--white);
  }
  .cover__hero {
    position: absolute; left: 0; top: 0;
    width: 1033px; height: 394px;
    background: var(--cover-black);
    overflow: hidden;
  }
  .hero__side {
    position: absolute; top: 0; height: 394px;
  }
  .hero__side--left {
    left: 0; width: 290px;
    background: linear-gradient(90deg, var(--cover-black) 0%, var(--green-tint) 45%, var(--green-tint) 70%, var(--cover-black) 100%);
  }
  .hero__side--right {
    left: 755px; width: 278px;
    background: linear-gradient(90deg, var(--cover-black) 0%, var(--teal-tint) 35%, var(--teal-tint) 70%, var(--cover-black) 100%);
  }

  .brand__dot {
    position: absolute; left: 328px; top: 47px;
    width: 90px; height: 90px; border-radius: 50%;
    background: linear-gradient(135deg, var(--neon-green), var(--deep-blue));
  }
  .brand__name {
    position: absolute; left: 441px; top: 51px;
    display: flex; flex-direction: column;
    font-family: "Montserrat", sans-serif; font-weight: 500;
    color: var(--white); line-height: 1;
  }
  .brand__word { font-size: 44px; letter-spacing: 2px; }
  .brand__sub { font-size: 25px; margin-top: 6px; }

  .tagline {
    position: absolute; left: 8px; right: 0; top: 180px;
    text-align: center;
    font-family: "Montserrat", sans-serif; font-weight: 800;
    font-size: 29px; line-height: 54px;
  }
  .tagline span {
    display: inline-block;
    background: linear-gradient(90deg, var(--neon-green) 0%, var(--neon-green) 45%, var(--aqua) 100%);
    -webkit-background-clip: text; background-clip: text;
    color: transparent;
  }

  .profile {
    position: absolute; left: 65px; top: 224px;
    width: 229px; height: 229px;
    background: var(--white);
    padding: 8px;
  }
  .profile__panel {
    position: relative; width: 100%; height: 100%;
    background: linear-gradient(135deg, var(--profile-grey-a), var(--profile-grey-b));
  }
  .profile__dot {
    position: absolute; left: 15px; top: 86px;
    width: 44px; height: 44px; border-radius: 50%;
    background: linear-gradient(135deg, var(--neon-green), var(--deep-blue));
  }
  .profile__name {
    position: absolute; left: 69px; top: 89px;
    display: flex; flex-direction: column; line-height: 1;
    font-family: "Montserrat", sans-serif; font-weight: 500;
    color: var(--ink-dark);
  }
  .profile__word { font-size: 21px; letter-spacing: 0.5px; }
  .profile__sub { font-size: 12px; margin-top: 4px; }

  .contact {
    position: absolute; top: 411px; height: 32px;
    display: flex; align-items: center;
    font-family: "Roboto", sans-serif; font-size: 17px;
    color: var(--contact-blue);
  }
  .contact__icon { width: 32px; height: 32px; flex: none; }
  .contact--phone { left: 323px; }
  .contact--phone .contact__text { margin-left: 16px; }
  .contact--web { left: 555px; }
  .contact--web .contact__text { margin-left: 11px; }
  .contact--mail { left: 805px; }
  .contact--mail .contact__text { margin-left: 19px; }
</style>
</head>
<body>
  <main class="cover">
    <section class="cover__hero">
      <div class="hero__side hero__side--left" role="img" aria-label="Decorative pattern of green vertical circuit lines"></div>
      <div class="hero__side hero__side--right" role="img" aria-label="Decorative pattern of teal vertical circuit lines"></div>

      <span class="brand__dot"></span>
      <div class="brand__name">
        <span class="brand__word">OLVENDRA</span>
        <span class="brand__sub">Technologies GmbH</span>
      </div>

      <h1 class="tagline">
        <span>EMPOWERING TECHNOLOGY</span><br>
        <span>ENABLING SUCCESS</span>
      </h1>
    </section>

    <aside class="profile">
      <div class="profile__panel" role="img" aria-label="Profile picture with company name on light grey background with faint line pattern">
        <span class="profile__dot"></span>
        <div class="profile__name">
          <span class="profile__word">OLVENDRA</span>
          <span class="profile__sub">Technologies GmbH</span>
        </div>
      </div>
    </aside>

    <div class="contact contact--phone">
      <svg class="contact__icon" viewBox="0 0 24 24" aria-hidden="true">
        <path fill="var(--contact-blue)" d="M6.6 2.2c.6-.4 1.4-.3 1.8.3l2.1 3.2c.4.6.3 1.4-.2 1.8L9 8.6c.9 2.4 3.4 5.3 6.1 6.6l1.3-1.2c.5-.5 1.3-.5 1.8-.1l3 2.3c.6.4.7 1.2.3 1.8l-1.4 2.1c-.6.9-1.7 1.3-2.7 1C9.9 19 4.9 13.4 3.4 6.5c-.2-1 .2-2 1.1-2.6z"/>
      </svg>
      <span class="contact__text">+44 0000 000000</span>
    </div>
    <div class="contact contact--web">
      <svg class="contact__icon" viewBox="0 0 24 24" aria-hidden="true">
        <g fill="none" stroke="var(--contact-blue)" stroke-width="1.6">
          <circle cx="12" cy="12" r="10.5"/>
          <ellipse cx="12" cy="12" rx="4.6" ry="10.5"/>
          <line x1="12" y1="1.5" x2="12" y2="22.5"/>
          <line x1="1.5" y1="12" x2="22.5" y2="12"/>
          <path d="M3.2 6.5 H20.8 M3.2 17.5 H20.8"/>
        </g>
      </svg>
      <span class="contact__text">www.loremipsum.com</span>
    </div>
    <div class="contact contact--mail">
      <svg class="contact__icon" viewBox="0 0 24 24" aria-hidden="true">
        <rect x="1" y="4.5" width="22" height="15" fill="var(--contact-blue)"/>
        <path d="M1 4.5 L12 13.5 L23 4.5 M1 19.5 L9.2 11.3 M23 19.5 L14.8 11.3" fill="none" stroke="#ffffff" stroke-width="1.3"/>
      </svg>
      <span class="contact__text">lorem@ipsum.com</span>
    </div>
  </main>
</body>
</html>
```